Brimovex business card

Based on company logo and website given , to design a business card temple. Slogan "Your furry friends deserves the best"
Color style please refer to our website

```html
<!DOCTYPE html>
<html lang="en">
<head>
<meta charset="utf-8">
<title>Brimovex business card</title>
<link rel="stylesheet" href="https://fonts.googleapis.com/css2?family=Rubik:wght@300;400;500&display=swap">
<style>
  :root {
    --canvas-bg: #3a3a3c;
    --card-dark: #0a2c2c;
    --logo-teal: #2a7f84;
    --card-light: #f1f0f4;
    --brand-gold: #b5aa2c;
    --ink-dark: #0d2a2a;
    --ink-grey: #5a5a60;
  }
  * { box-sizing: border-box; margin: 0; padding: 0; }
  html, body {
    width: 1200px; height: 900px; overflow: hidden;
    background: var(--canvas-bg);
    font-family: "Rubik", sans-serif;
  }
  .sheet {
    width: 1200px; height: 900px;
    display: flex; flex-direction: column; align-items: center; justify-content: center;
    gap: 46px;
  }
  .card {
    width: 660px; height: 378px;
    position: relative;
    box-shadow: 0 10px 28px rgba(0,0,0,0.45);
  }
  .card--front {
    background: var(--card-dark);
    display: flex; align-items: center; justify-content: center;
  }
  .card--front .wordmark {
    color: var(--logo-teal);
    font-size: 64px; font-weight: 500; letter-spacing: 1px;
  }
  .card--back { background: var(--card-light); }
  .card--back .wordmark {
    position: absolute; left: 70px; top: 160px;
    color: var(--brand-gold);
    font-size: 54px; font-weight: 500; letter-spacing: 1px;
  }
  .contact {
    position: absolute; left: 370px; top: 70px;
    color: var(--ink-grey);
  }
  .contact__name {
    color: var(--ink-dark);
    font-size: 17px; font-weight: 500; letter-spacing: 0.5px; text-transform: uppercase;
  }
  .contact__role { font-size: 13px; font-weight: 300; margin-top: 1px; }
  .contact__address {
    font-size: 13px; font-weight: 300; line-height: 1.45;
    margin: 22px 0 0 22px; font-style: normal;
  }
  .contact__list {
    list-style: none; margin: 22px 0 0 42px;
    font-size: 14px; font-weight: 300; line-height: 1.6;
  }
  .contact__list li { display: flex; align-items: center; gap: 10px; }
  .contact__list svg { width: 13px; height: 13px; fill: var(--brand-gold); flex: none; }
</style>
</head>
<body>
<main class="sheet">
  <section class="card card--front" aria-label="Card front">
    <span class="wordmark">Brimovex</span>
  </section>

  <section class="card card--back" aria-label="Card back">
    <span class="wordmark">Brimovex</span>
    <div class="contact">
      <p class="contact__name">Owen Marlowe</p>
      <p class="contact__role">Director</p>
      <address class="contact__address">12/40 Harlow Street<br>Glenmore Vic 3188</address>
      <ul class="contact__list">
        <li>
          <svg viewBox="0 0 16 16" aria-hidden="true"><path d="M3.6 1.2l2.3 2.6-1.3 1.9c.9 2 2.7 3.8 4.7 4.7l1.9-1.3 2.6 2.3-1.4 2.3C7 13.4 2.6 9 1.3 3z"/></svg>
          +61 3 9047 4182
        </li>
        <li>
          <svg viewBox="0 0 16 16" aria-hidden="true"><path d="M4 1h8v14H4zM5.5 2.5v9h5v-9zM7.3 12.5h1.4v1.4H7.3z" fill-rule="evenodd"/></svg>
          1800 310 245
        </li>
        <li>
          <svg viewBox="0 0 16 16" aria-hidden="true"><path d="M1 3.5h14v9H1zM1.6 4l6.4 5 6.4-5"/></svg>
          sales@brimovex.com.au
        </li>
        <li>
          <svg viewBox="0 0 16 16" aria-hidden="true"><circle cx="8" cy="8" r="7"/><path d="M1 8h14M8 1c-2.5 2-2.5 12 0 14M8 1c2.5 2 2.5 12 0 14" stroke="#f1f0f4" stroke-width="1" fill="none"/></svg>
          www.brimovex.com.au
        </li>
      </ul>
    </div>
  </section>
</main>
</body>
</html>
```